New Business Card Design Project

Target Market(s)

Passing cards out

Industry/Entity Type

Asphalt contractor

Contact Information for Business Card

Ridgefold Paving

Colors
FFC000
F8CF3A
FAE287
FDF2CF
FEFAEE
F0912C
F2A743
F7CA91
FBE8D2
FDF5EE
EE7325
F08F49
F5BC92
FAE3D3
FDF4ED

Requirements
Must have
• Asphalt
Nice to have
• Would like to have 2 pictures on it of equipment

```html
<!DOCTYPE html>
<html lang="en">
<head>
<meta charset="utf-8">
<title>Ridgefold Paving – Business Card</title>
<link rel="stylesheet" href="https://fonts.googleapis.com/css2?family=Montserrat:wght@500;600;800&display=swap">
<style>
  :root {
    --brand-orange: #ee7325;
    --brand-amber: #f0912c;
    --brand-yellow: #ffc000;
    --ink: #1c1c1c;
    --card: #ffffff;
    --backdrop: #e6e4e1;
    --equip-dark: #3a3a3a;
  }
  html, body {
    margin: 0;
    width: 1200px;
    height: 1200px;
    overflow: hidden;
    background: var(--backdrop);
    font-family: "Montserrat", sans-serif;
  }
  .canvas {
    position: relative;
    width: 1200px;
    height: 1200px;
  }
  .card {
    position: absolute;
    left: 254px;
    width: 692px;
    height: 402px;
    background: var(--card);
    box-sizing: border-box;
  }
  .card--front { top: 150px; }
  .card--back  { top: 650px; }

  /* Front */
  .brand-name {
    position: absolute;
    top: 96px;
    left: 0;
    right: 0;
    display: flex;
    justify-content: center;
    align-items: center;
    gap: 18px;
    white-space: nowrap;
  }
  .brand-name__dot {
    width: 38px;
    height: 38px;
    border-radius: 50%;
    background: var(--brand-yellow);
    flex: none;
  }
  .brand-name__text {
    font-weight: 800;
    font-size: 48px;
    color: var(--brand-orange);
    text-transform: uppercase;
    line-height: 1;
  }
  .equipment {
    position: absolute;
    top: 232px;
    width: 170px;
    height: 100px;
    border-radius: 6px;
    background: linear-gradient(180deg, var(--brand-orange) 0%, var(--brand-amber) 62%, var(--equip-dark) 100%);
  }
  .equipment--paver { left: 46px; }
  .equipment--truck { right: 46px; }
  .service-label {
    position: absolute;
    top: 262px;
    left: 50%;
    transform: translateX(-50%);
    padding: 6px 18px;
    border: 3px solid var(--ink);
    border-radius: 6px;
    background: var(--brand-yellow);
    font-weight: 800;
    font-size: 28px;
    line-height: 1.1;
    color: var(--ink);
    letter-spacing: 2px;
    text-transform: uppercase;
  }

  /* Back */
  .contact-name {
    position: absolute;
    left: 50px;
    top: 50px;
    margin: 0;
    font-weight: 600;
    font-size: 44px;
    line-height: 1.2;
    color: var(--brand-orange);
  }
  .contact-role {
    position: absolute;
    left: 50px;
    top: 112px;
    margin: 0;
    font-weight: 500;
    font-size: 24px;
    color: var(--brand-amber);
  }
  .divider {
    position: absolute;
    left: 50px;
    top: 158px;
    width: 58px;
    height: 3px;
    background: var(--brand-yellow);
  }
  .contact-list {
    position: absolute;
    left: 48px;
    top: 186px;
    margin: 0;
    padding: 0;
    list-style: none;
  }
  .contact-list li {
    display: flex;
    align-items: center;
    gap: 16px;
    height: 48px;
    font-weight: 500;
    font-size: 24px;
    color: var(--ink);
    white-space: nowrap;
  }
  .contact-list svg {
    width: 26px;
    height: 26px;
    fill: var(--brand-orange);
    flex: none;
  }
  .accent {
    position: absolute;
    background: var(--brand-orange);
  }
  .accent--top { right: 44px; top: 0; width: 8px; height: 50px; background: var(--brand-yellow); }
  .accent--bottom { right: 0; bottom: 46px; width: 48px; height: 8px; }
</style>
</head>
<body>
<main class="canvas">
  <section class="card card--front">
    <div class="brand-name">
      <span class="brand-name__dot"></span>
      <span class="brand-name__text">Ridgefold Paving</span>
    </div>
    <div class="equipment equipment--paver" role="img" aria-label="Illustration of an asphalt paving machine"></div>
    <div class="service-label">Asphalt</div>
    <div class="equipment equipment--truck" role="img" aria-label="Illustration of a dump truck loaded with asphalt"></div>
  </section>

  <section class="card card--back">
    <h1 class="contact-name">Dale Harmon</h1>
    <p class="contact-role">Site Supervisor</p>
    <div class="divider"></div>
    <ul class="contact-list">
      <li>
        <svg viewBox="0 0 24 24" aria-hidden="true"><path d="M6.6 10.8a15.1 15.1 0 0 0 6.6 6.6l2.2-2.2a1 1 0 0 1 1-.25 11.4 11.4 0 0 0 3.6.57 1 1 0 0 1 1 1V20a1 1 0 0 1-1 1A17 17 0 0 1 3 4a1 1 0 0 1 1-1h3.5a1 1 0 0 1 1 1c0 1.25.2 2.45.57 3.57a1 1 0 0 1-.25 1z"/></svg>
        (555) 418-2760
      </li>
      <li>
        <svg viewBox="0 0 24 24" aria-hidden="true"><path d="M2 5h20v14H2z M4 7v.5l8 5 8-5V7l-8 5z" fill-rule="evenodd"/></svg>
        dale@ridgefoldpaving.com
      </li>
      <li>
        <svg viewBox="0 0 24 24" aria-hidden="true"><path d="M12 2a7 7 0 0 0-7 7c0 5.2 7 13 7 13s7-7.8 7-13a7 7 0 0 0-7-7zm0 9.5A2.5 2.5 0 1 1 12 6.5a2.5 2.5 0 0 1 0 5z"/></svg>
        2140 Quarry Ln, Denver, CO 80216
      </li>
      <li>
        <svg viewBox="0 0 24 24" aria-hidden="true"><path d="M12 2a10 10 0 1 0 0 20 10 10 0 0 0 0-20zm6.9 6h-3a15.6 15.6 0 0 0-1.4-3.6A8 8 0 0 1 18.9 8zM12 4a14 14 0 0 1 1.9 4h-3.8A14 14 0 0 1 12 4zM4.3 14a8 8 0 0 1 0-4h3.4a16 16 0 0 0 0 4zm.8 2h3a15.6 15.6 0 0 0 1.4 3.6A8 8 0 0 1 5.1 16zm3-8h-3a8 8 0 0 1 4.4-3.6A15.6 15.6 0 0 0 8.1 8zM12 20a14 14 0 0 1-1.9-4h3.8A14 14 0 0 1 12 20zm2.3-6H9.7a14.7 14.7 0 0 1 0-4h4.6a14.7 14.7 0 0 1 0 4zm.2 5.6a15.6 15.6 0 0 0 1.4-3.6h3a8 8 0 0 1-4.4 3.6zm1.8-5.6a16 16 0 0 0 0-4h3.4a8 8 0 0 1 0 4z"/></svg>
        www.ridgefoldpaving.com
      </li>
    </ul>
    <span class="accent accent--top"></span>
    <span class="accent accent--bottom"></span>
  </section>
</main>
</body>
</html>
```